Business Card

Yes I would like you to design me a business card with the logo you just made me

Industry/Entity Type

Business

Colors
33b7a4
00a990
333333
000000
757575
7f7f7f

```html
<!DOCTYPE html>
<html lang="en">
<head>
<meta charset="utf-8">
<title>Lena Marlow Photography – Business Card</title>
<link rel="stylesheet" href="https://fonts.googleapis.com/css2?family=Open+Sans:wght@400;600&family=Cinzel:wght@400&display=swap">
<style>
  :root {
    --teal: #00a990;
    --teal-light: #33b7a4;
    --charcoal: #333333;
    --ink: #000000;
    --grey: #757575;
    --grey-soft: #7f7f7f;
    --card-back: #3a3c3e;
    --paper: #ffffff;
    --stage: #e9e9e7;
  }
  * { margin: 0; padding: 0; box-sizing: border-box; }
  html, body {
    width: 1200px; height: 784px; overflow: hidden;
    background: var(--stage);
    font-family: "Open Sans", Arial, sans-serif;
  }
  .stage {
    position: relative; width: 1200px; height: 784px;
    display: flex; align-items: center; justify-content: center; gap: 60px;
  }
  .card {
    position: relative; width: 520px; height: 298px;
    border-radius: 2px; overflow: hidden;
    box-shadow: 0 6px 18px rgba(0,0,0,0.18);
  }
  /* Back side */
  .card--back { background: var(--card-back); }
  .card__watermark {
    position: absolute; right: 60px; top: 40px;
    width: 150px; height: 150px; border-radius: 50%;
    background: rgba(255,255,255,0.035);
  }
  .card__footer {
    position: absolute; left: 26px; bottom: 52px;
    display: flex; align-items: center; gap: 14px;
  }
  .brand-small { display: flex; flex-direction: column; align-items: center; color: var(--teal); }
  .brand-small__dot {
    width: 22px; height: 22px; border-radius: 50%; background: var(--teal); margin-bottom: 3px;
  }
  .brand-small__name { font-size: 24px; font-weight: 400; line-height: 1; letter-spacing: 0.5px; }
  .brand-small__tag {
    font-family: "Cinzel", Georgia, serif; font-size: 8px; letter-spacing: 3px; margin-top: 3px;
  }
  .divider { width: 1px; height: 60px; background: var(--grey-soft); }
  .contact { list-style: none; color: #e6e6e6; font-size: 12.5px; line-height: 19px; }
  .contact li { display: flex; align-items: center; gap: 7px; }
  .contact svg { width: 11px; height: 11px; flex: none; }
  .contact .square { width: 10px; height: 10px; background: var(--teal); flex: none; }
  /* Front side */
  .card--front { background: var(--paper); }
  .brand {
    position: absolute; left: 0; right: 0; top: 78px;
    display: flex; flex-direction: column; align-items: center; color: var(--charcoal);
  }
  .brand__dot {
    width: 40px; height: 40px; border-radius: 50%; background: var(--charcoal); margin-bottom: 10px;
  }
  .brand__name { font-size: 50px; font-weight: 400; line-height: 1; letter-spacing: 1px; }
  .brand__tag {
    font-family: "Cinzel", Georgia, serif; font-size: 15px; letter-spacing: 7px; margin-top: 8px;
  }
</style>
</head>
<body>
<main class="stage">
  <section class="card card--back" aria-label="Business card back">
    <div class="card__watermark" aria-hidden="true"></div>
    <div class="card__footer">
      <div class="brand-small">
        <span class="brand-small__dot"></span>
        <span class="brand-small__name">lena marlow</span>
        <span class="brand-small__tag">PHOTOGRAPHY</span>
      </div>
      <span class="divider"></span>
      <ul class="contact">
        <li>
          <svg viewBox="0 0 12 12" aria-hidden="true"><rect x="2.5" y="0.5" width="7" height="11" rx="1.2" fill="none" stroke="var(--teal)" stroke-width="1.3"/><circle cx="6" cy="9.4" r="0.8" fill="var(--teal)"/></svg>
          555-204-7193
        </li>
        <li>
          <svg viewBox="0 0 12 12" aria-hidden="true"><rect x="0.6" y="2" width="10.8" height="8" fill="none" stroke="var(--teal)" stroke-width="1.2"/><path d="M0.8 2.4 6 6.6 11.2 2.4" fill="none" stroke="var(--teal)" stroke-width="1.2"/></svg>
          lenamarlowphoto@mail.com
        </li>
        <li><span class="square" aria-hidden="true"></span>lenamarlowphotography</li>
      </ul>
    </div>
  </section>

  <section class="card card--front" aria-label="Business card front">
    <div class="brand">
      <span class="brand__dot"></span>
      <span class="brand__name">lena marlow</span>
      <span class="brand__tag">PHOTOGRAPHY</span>
    </div>
  </section>
</main>
</body>
</html>
```